A Hair, Beauty and Nails Wholesalers Needs a Business Card Design

We need a business card design for our company which is being passed from parents to daughter, so we wont to re-launch the company with an updated, modern, sophisticated, elegant, chic and fresh look which still incorporates the original colour scheme of Hot Pink, Dark Grey and White. The original logo which is attached can be used on the card but we would like to see some designs with the logo and some without, as we have not yet decided if we want the logo on the card. The name of our company is 'Velmora Supplies' and the name of our website is VelmoraGlowandPolish.example.au. We specialise in supplying a massive range of Hair, Beauty and Nail products to the industry. We are based in QLD, Australia but ship many orders via our website all across Australia.

```html
<!DOCTYPE html>
<html lang="en">
<head>
<meta charset="utf-8">
<title>Velmora Supplies – Business Card</title>
<link rel="stylesheet" href="https://fonts.googleapis.com/css2?family=Open+Sans:wght@400;600;700&display=swap">
<style>
  :root {
    --hot-pink: #e60ab4;
    --hot-pink-deep: #c9079c;
    --hot-pink-light: #f23ccb;
    --dark-grey: #2b2b2b;
    --mid-grey: #555555;
    --white: #ffffff;
    --paper: #f7f7f7;
    --backdrop: #e9e6e3;
  }
  * { box-sizing: border-box; margin: 0; padding: 0; }
  html, body {
    width: 1200px; height: 1023px; overflow: hidden;
    background: var(--backdrop);
    font-family: "Open Sans", Arial, sans-serif;
  }
  .sheet {
    position: relative; width: 1200px; height: 1023px;
  }
  .card {
    position: absolute; left: 260px; width: 680px; height: 416px;
    border-radius: 34px; overflow: hidden;
    box-shadow: 0 12px 30px rgba(0,0,0,0.18);
  }
  .card--front { top: 52px; background: linear-gradient(160deg, var(--white), var(--paper)); }
  .card--back {
    top: 552px;
    background: linear-gradient(200deg, var(--hot-pink-light) 0%, var(--hot-pink) 45%, var(--hot-pink-deep) 100%);
  }
  .swoosh { position: absolute; inset: 0; width: 100%; height: 100%; }

  .brand {
    position: absolute; left: 58px; top: 118px;
    display: flex; align-items: center; gap: 14px;
  }
  .brand__dot {
    width: 20px; height: 20px; border-radius: 50%; background: var(--hot-pink);
  }
  .brand__name {
    font-weight: 700; font-size: 38px; color: var(--dark-grey); letter-spacing: 0.5px;
  }
  .person {
    position: absolute; left: 58px; top: 196px;
    font-size: 22px; color: var(--dark-grey);
  }
  .person__name { font-weight: 700; }
  .person__role { font-weight: 400; font-size: 15px; color: var(--mid-grey); }
  .person__bar { color: var(--mid-grey); font-weight: 400; margin: 0 6px; }

  .contacts {
    position: absolute; left: 58px; top: 246px; list-style: none;
    font-size: 13.5px; color: var(--mid-grey); line-height: 1;
  }
  .contacts li { display: flex; align-items: center; gap: 10px; margin-bottom: 9px; }
  .contacts svg { width: 16px; height: 16px; flex: none; }

  .address {
    position: absolute; right: 52px; top: 44px; text-align: left;
    font-size: 13.5px; line-height: 1.45; color: var(--dark-grey);
  }
  .address__company { font-weight: 700; }

  .back-brand {
    position: absolute; left: 62px; top: 60px;
    display: flex; align-items: center; gap: 16px;
  }
  .back-brand__dot { width: 22px; height: 22px; border-radius: 50%; background: var(--dark-grey); }
  .back-brand__name { font-weight: 700; font-size: 46px; color: var(--dark-grey); letter-spacing: 0.5px; }
</style>
</head>
<body>
<main class="sheet">

  <section class="card card--front" aria-label="Business card front">
    <svg class="swoosh" viewBox="0 0 680 416" preserveAspectRatio="none">
      <path d="M300 416 C 430 360, 560 260, 680 92 L 680 416 Z" fill="#e60ab4" opacity="0.92"
            role="img" aria-label="Pattern of pink hair, beauty and nail tools: combs, scissors, dryers, polish bottles"/>
      <path d="M292 416 C 425 352, 552 252, 672 78" fill="none" stroke="#2b2b2b" stroke-width="5" stroke-linecap="round"/>
    </svg>

    <div class="address">
      <div class="address__company">Velmora Supplies</div>
      <div>58 Larkspur Lane,</div>
      <div>Brindlewood QLD 4999</div>
      <div>Australia.</div>
    </div>

    <div class="brand">
      <span class="brand__dot"></span>
      <span class="brand__name">Velmora Supplies</span>
    </div>

    <div class="person">
      <span class="person__name">Mara Ellison</span><span class="person__bar">|</span><span class="person__role">Director</span>
    </div>

    <ul class="contacts">
      <li>
        <svg viewBox="0 0 16 16"><circle cx="8" cy="8" r="8" fill="#e60ab4"/><path d="M5.2 4.2l1.5 1.6-.7 1c.6 1.2 1.5 2.1 2.7 2.7l1-.7 1.6 1.5-.9 1.3C7.8 11.4 4.6 8.2 4 5.1z" fill="#fff"/></svg>
        07 5550 0192
      </li>
      <li>
        <svg viewBox="0 0 16 16"><circle cx="8" cy="8" r="8" fill="#e60ab4"/><rect x="4" y="5.2" width="8" height="5.6" rx="0.6" fill="#fff"/><path d="M4.2 5.5L8 8.5l3.8-3" fill="none" stroke="#e60ab4" stroke-width="0.9"/></svg>
        info@velmoraglowandpolish.example.au
      </li>
      <li>
        <svg viewBox="0 0 16 16"><circle cx="8" cy="8" r="8" fill="#e60ab4"/><circle cx="8" cy="8" r="4" fill="none" stroke="#fff" stroke-width="1"/><path d="M4 8h8M8 4c-1.6 2.4-1.6 5.6 0 8M8 4c1.6 2.4 1.6 5.6 0 8" fill="none" stroke="#fff" stroke-width="0.8"/></svg>
        www.VelmoraGlowandPolish.example.au
      </li>
    </ul>
  </section>

  <section class="card card--back" aria-label="Business card back">
    <div class="back-brand">
      <span class="back-brand__dot"></span>
      <span class="back-brand__name">Velmora Supplies</span>
    </div>
  </section>

</main>
</body>
</html>
```